Grey Heron Estates Inc Business Card design

Grey Heron Estates Inc is a West Vancouver based boutique brokerage specializing in the marketing and sale of luxury and waterfront real estate.

This card is for Marlon Tevaki, Vice-President.

The card should have something modern and unique about. Some sort of gimmick would be nice.

I would like it to use or update the grey heron estates logo visible at www.greyheronestates-example.com

Very open to any design.

Target Market(s)

humans, the type with money

Industry/Entity Type

Marketing

Requirements
Must have
• The name Marlon Tevaki

Company name Grey Heron Estates Inc

Phone 604-512-3047

Fax 604-488-1630

email marlontevaki@mailbox-example.com

website www.marlontevaki-example.com

LOGO

tag line"a fresh approach to real estate in west vancouver"

the attched pic of me if possible
Nice to have
• Something that would make people say "nice card" and not throw it in the garbage immediately, open to ideas
Should not have
• anything that looks like a template

```html
<!DOCTYPE html>
<html lang="en">
<head>
<meta charset="utf-8">
<title>Grey Heron Estates Inc — Marlon Tevaki</title>
<link rel="stylesheet" href="https://fonts.googleapis.com/css2?family=Marcellus&family=Lustria&family=Tinos&display=swap">
<style>
  :root {
    --ink: #000000;
    --frame: #ffffff;
    --silver-light: #f2f2f2;
    --silver-mid: #9a9a9a;
    --silver-dark: #3c3c3c;
    --band-light: #c8c8c8;
    --band-dark: #4a4a4a;
    --band-edge: #f4f4f4;
    --contact-ink: #111111;
  }
  html, body {
    margin: 0;
    padding: 0;
    width: 1200px;
    height: 742px;
    overflow: hidden;
    background: var(--frame);
  }
  .card {
    position: relative;
    width: 1200px;
    height: 742px;
    background: var(--ink);
    border-radius: 22px;
    overflow: hidden;
  }
  .card-frame {
    position: absolute;
    left: 15px;
    top: 15px;
    right: 15px;
    bottom: 15px;
    border: 2px solid var(--frame);
    border-radius: 16px;
    overflow: hidden;
  }
  .brand-name {
    position: absolute;
    left: 0;
    right: 0;
    top: 232px;
    margin: 0;
    text-align: center;
    font-family: "Marcellus", serif;
    font-weight: 400;
    font-size: 48px;
    font-variant: small-caps;
    letter-spacing: 1px;
    color: var(--silver-mid);
  }
  .tagline {
    position: absolute;
    left: 0;
    right: 0;
    top: 290px;
    margin: 0;
    text-align: center;
    font-family: "Marcellus", serif;
    font-size: 25px;
    text-transform: uppercase;
    letter-spacing: 1.2px;
    background: linear-gradient(90deg, var(--silver-dark) 0%, var(--silver-light) 45%, var(--silver-mid) 75%, var(--silver-light) 100%);
    -webkit-background-clip: text;
    background-clip: text;
    color: transparent;
  }
  .agent-name {
    position: absolute;
    left: 0;
    right: 0;
    top: 408px;
    margin: 0;
    text-align: center;
    font-family: "Lustria", serif;
    font-weight: 400;
    font-size: 76px;
    letter-spacing: 0.5px;
    background: linear-gradient(90deg, var(--silver-mid) 0%, var(--silver-light) 30%, var(--silver-dark) 55%, var(--silver-light) 85%, var(--silver-mid) 100%);
    -webkit-background-clip: text;
    background-clip: text;
    color: transparent;
  }
  .contact-band {
    position: absolute;
    left: 0;
    right: 0;
    bottom: 0;
    height: 111px;
    background: linear-gradient(90deg, var(--band-light) 0%, var(--band-light) 20%, var(--band-dark) 55%, var(--band-light) 85%, var(--band-edge) 100%);
    font-family: "Tinos", serif;
    font-size: 35px;
    line-height: 43px;
    color: var(--contact-ink);
  }
  .contact-phone {
    position: absolute;
    left: 61px;
    top: 12px;
  }
  .contact-web {
    position: absolute;
    right: 60px;
    top: 12px;
    text-align: right;
  }
  .contact-band p { margin: 0; }
</style>
</head>
<body>
  <div class="card">
    <div class="card-frame">
      <h1 class="brand-name">Grey Heron Estates Inc.</h1>
      <p class="tagline">A fresh approach to real estate in West Vancouver</p>
      <h2 class="agent-name">Marlon Tevaki</h2>
      <div class="contact-band">
        <div class="contact-phone">
          <p>Phone 604-512-3047</p>
          <p>Fax 604-488-1630</p>
        </div>
        <div class="contact-web">
          <p>marlontevaki@mailbox-example.com</p>
          <p>www.marlontevaki-example.com</p>
        </div>
      </div>
    </div>
  </div>
</body>
</html>
```